Informational Trifold Flyer to Highlight Our After-School Program Curriculum

We need a trifold to hand out to families at our open house events that highlights our programs and curriculum. We provide quality, nationally recognized, award winning child development programs and after school care affordable to every family at any income level. Our programs include curriculum in Education & Career Development, STEM, the Arts, Academic Support, Character & Leadership, Health & Life Skills, Sports & Recreation.

Our curriculum is designed to be fun AND purposeful.

Our target market is parents of children ages 4-13 years old of every socioeconomic background. The brochure needs to be inclusive, eye-catching, family friendly, professional and informative.

I'm uploading our current curriculum guide for a sense of the flyer's CONTENT ONLY. Please DO NOT copy the design in the Curriculum Guide upload - we plan to redesign it soon. Please DO USE the Success Statistics in the Curriculum Guide.

I'm also uploading some of our recent flyer designs for a sense of the look and feel that we like. Also uploading our logo, some other branded assets, and a branding guideline that can be referred to for colors, fonts and logo spacing. The logo is the only required asset. The colors listed in the guideline are not required. The brand fonts are not required either but using them is a good idea, unless they just don't work with your creative vision.

I can provide logo files and other assets as psd files for final flyer.

We have around 10 flyers we need designed each year so this project can lead to regular, ongoing work.

Target Market(s)

Parents of children ages 4-13

Industry/Entity Type

Non-profit child care and child development

Font styles to use
Serif
Sans Serif
Other font styles liked:
• Franklin Gothic Book URW - Book, Franklin Gothic URW - Demi, Museo Slab - 1000, Helvetica - Regular, Arial Regular

Requirements
Must have
• Logo. Inclusive, family friendly. Ability to edit brochure based on location. Success Statistics Highlighted (see curriculum guide for content). Room for list of core programs. Quotes from parents. Register online: URL (will vary by location).
Nice to have
• It would be nice to be able to feature a few different aspects of program in detail, or show a curriculum project. Can provide content for such.
Should not have
• Anything that is not inclusive or family friendly.

```html
<!DOCTYPE html>
<html lang="en">
<head>
<meta charset="utf-8">
<title>After School Curriculum Guide Trifold</title>
<link href="https://fonts.googleapis.com/css2?family=Roboto:wght@400;700&family=Roboto+Condensed:wght@700&family=Luckiest+Guy&display=swap" rel="stylesheet">
<style>
:root{
  --cyan:#00c2e6;
  --sky:#a9d8f5;
  --blue:#1a8fd8;
  --green:#2e8b3a;
  --yellow:#f7b731;
  --red:#d8322a;
  --purple:#4b2a8a;
  --paper:#f6f7f8;
  --ink:#333;
  --white:#fff;
}
*{box-sizing:border-box;margin:0;padding:0}
html,body{width:800px;height:1200px;overflow:hidden;background:#ececec;font-family:"Roboto",Arial,sans-serif;color:var(--ink)}
.spread{position:absolute;left:20px;width:760px;height:538px;overflow:hidden;box-shadow:0 4px 14px rgba(0,0,0,.18)}
.spread.outside{top:40px}
.spread.inside{top:622px}
.panel{position:absolute;top:0;width:254px;height:538px;overflow:hidden}
.p1{left:0}.p2{left:253px}.p3{left:506px}
.photo{position:absolute;background:linear-gradient(135deg,#8a9aa6,#c9b9a3 55%,#6f8c7b)}
.deco{position:absolute;left:0;top:0}
h2.section{font-family:"Roboto Condensed",Arial,sans-serif;color:var(--cyan);font-size:13px;position:absolute;left:22px}
/* FAQ */
.faq-list{position:absolute;left:22px;top:60px;width:212px;list-style:none;font-size:5.6px;line-height:1.65}
.faq-list li{position:relative;padding-left:12px;margin-bottom:2px}
.faq-list li::before{content:"";position:absolute;left:0;top:1px;width:6px;height:6px;border:1.5px solid var(--blue);border-radius:50%}
.faq-list b{display:block;font-weight:700}
/* contact panel */
.quote-box{position:absolute;left:22px;top:22px;width:210px;height:118px;background:var(--white);outline:1px solid var(--cyan);outline-offset:-7px;text-align:center;padding:26px 18px 0;font-size:10px;line-height:1.25}
.quote-box .mark{position:absolute;left:0;right:0;font-family:Georgia,serif;font-weight:700;font-size:22px;line-height:1;color:#222}
.quote-box .mark.open{top:6px}.quote-box .mark.close{bottom:4px}
.quote-box cite{display:block;font-style:normal;font-weight:700;margin-top:2px}
.blank-box{position:absolute;left:22px;top:146px;width:210px;height:172px;background:var(--white)}
.brand{position:absolute;display:flex;align-items:center;gap:5px;font-family:"Roboto",Arial,sans-serif;font-weight:700;letter-spacing:.3px;white-space:nowrap}
.brand .dot{width:11px;height:11px;border-radius:50%}
.contact{position:absolute;left:0;width:254px;top:378px;text-align:center;color:var(--white);font-size:8.5px;line-height:1.3}
.contact h3{font-size:11px;margin-bottom:10px}
.contact p{margin-bottom:8px}
.contact svg{display:block;margin:0 auto 2px}
/* cover */
.title-box{position:absolute;left:30px;top:370px;width:196px;height:118px;background:var(--white);text-align:center;padding-top:8px;box-shadow:0 1px 3px rgba(0,0,0,.2)}
.title-box .line{display:block;font-family:"Luckiest Guy",Impact,sans-serif;line-height:1;white-space:nowrap}
.title-box .cyan{color:var(--cyan);font-size:22px}
.title-box .big{color:#111;font-size:40px;margin-top:3px}
.url{position:absolute;left:0;width:254px;text-align:center;color:var(--white);font-size:8px;font-weight:700}
/* programs */
.intro{position:absolute;left:22px;top:64px;width:212px;font-size:8px;line-height:1.35}
.lead{position:absolute;left:22px;top:170px;font-size:7.4px}
.core-list{position:absolute;left:22px;top:196px;list-style:none;font-size:7.4px}
.core-list li{display:flex;align-items:center;gap:8px;height:21px}
.core-list i{display:inline-block;width:11px;height:11px;border-radius:50%;background:var(--cyan)}
/* cards */
.card{position:absolute;background:var(--white);padding:4px;box-shadow:0 2px 5px rgba(0,0,0,.25)}
.card .photo{position:relative}
.cap{color:var(--white);padding:3px 5px 4px;font-size:4.4px;line-height:1.3;overflow:hidden}
.cap b{display:block;font-family:"Roboto Condensed",Arial,sans-serif;font-size:8.5px;line-height:1.1;margin-bottom:1px}
.tape{position:absolute;top:-6px;left:44%;width:40px;height:12px;background:#d8c79a;opacity:.85;transform:rotate(-4deg)}
</style>
</head>
<body>

<section class="spread outside">
  <div class="panel p1" style="background:var(--white)">
    <svg class="deco" width="254" height="538" viewBox="0 0 254 538" aria-hidden="true">
      <path d="M0 470 Q30 440 70 455 Q110 470 120 510 L130 538 L0 538Z" fill="var(--sky)"/>
      <path d="M200 500 Q230 490 254 498 L254 538 L190 538Z" fill="var(--sky)"/>
    </svg>
    <h2 class="section" style="top:30px">FAQ</h2>
    <ul class="faq-list">
      <li><b>Where are the Clubs located?</b>Bright Path Academy programs are located in the schools themselves. We partner with the schools to use their facilities.</li>
      <li><b>Do we help with homework and allow outside tutors to come into the Club?</b>Yes, one hour is dedicated to homework time Monday – Thursday and our staff and volunteers are there to assist if needed. We will allow outside tutors to come to the program, but they will have to complete the screening process we use for employees before they can interact with any child in our program.</li>
      <li><b>How do I enroll my child?</b>New parents, please create an account in our Parent Portal at www.brightpathacademy.org, then enroll your child for the desired location and services. Returning parents, please log in to your account in our Parent Portal, then select “Enroll my child” and choose the desired location and services.</li>
      <li><b>Can I enroll my additional children at a discounted fee?</b>Yes, please select the appropriate discount when you enroll your child.</li>
      <li><b>Will the program allow drop-in participants (children whose parents or day care are late picking up)?</b>We will allow one visit for free, but require the parent to pay for a daily package after the first time.</li>
      <li><b>What are the fees to enroll my child?</b>Fees are based on the market rate at your location and any discounts or reduced rates for which you qualify. A non-refundable payment for the first five days of services is due in order to complete your registration.</li>
    </ul>
    <div style="position:absolute;left:28px;top:418px;width:184px;height:92px;background:var(--green);transform:rotate(-4deg)"></div>
    <div class="photo" role="img" aria-label="Photo of children working on a craft project at a long table" style="left:30px;top:412px;width:178px;height:88px;transform:rotate(-5deg);background:linear-gradient(135deg,#d9c6a8,#f0ece4 50%,#b24b3a)"></div>
  </div>

  <div class="panel p2" style="background:var(--cyan)">
    <blockquote class="quote-box">
      <span class="mark open">“</span>
      I like that my daughter loves the program so much that she doesn’t want to leave when I go to pick her up
      <cite>-BPA Parent</cite>
      <span class="mark close">”</span>
    </blockquote>
    <div class="blank-box"></div>
    <div class="brand" style="left:58px;top:338px;color:var(--white);font-size:13px"><span class="dot" style="background:var(--white)"></span>BRIGHT PATH ACADEMY</div>
    <div class="contact">
      <h3>Contact Us</h3>
      <p><svg width="8" height="8" viewBox="0 0 24 24"><path fill="#fff" d="M6.6 10.8a15 15 0 0 0 6.6 6.6l2.2-2.2a1 1 0 0 1 1-.25 11.4 11.4 0 0 0 3.6.6 1 1 0 0 1 1 1V20a1 1 0 0 1-1 1A17 17 0 0 1 3 4a1 1 0 0 1 1-1h3.5a1 1 0 0 1 1 1c0 1.25.2 2.45.6 3.6a1 1 0 0 1-.25 1z"/></svg>555.210.4400</p>
      <p><svg width="8" height="8" viewBox="0 0 24 24"><path fill="#fff" d="M6 2h9v5H6zM3 8h18v10h-3v4H6v-4H3zm5 7v5h8v-5z"/></svg>1.555.318.7720</p>
      <p><svg width="8" height="8" viewBox="0 0 24 24"><circle cx="12" cy="12" r="9" fill="none" stroke="#fff" stroke-width="2"/><path d="M3 12h18M12 3c3 3 3 15 0 18M12 3c-3 3-3 15 0 18" fill="none" stroke="#fff" stroke-width="1.6"/></svg>www.brightpathacademy.org</p>
      <p><svg width="8" height="9" viewBox="0 0 24 24"><path fill="#fff" d="M12 2a7 7 0 0 0-7 7c0 5 7 13 7 13s7-8 7-13a7 7 0 0 0-7-7zm0 9.5A2.5 2.5 0 1 1 12 6.5a2.5 2.5 0 0 1 0 5z"/></svg>120 Maple Row<br>Fairview, ST 00410</p>
    </div>
  </div>

  <div class="panel p3" style="background:var(--paper)">
    <svg class="deco" width="254" height="538" viewBox="0 0 254 538" aria-hidden="true">
      <path d="M0 0 H80 Q60 30 20 40 Q0 45 0 70Z" fill="var(--sky)"/>
      <path d="M0 430 L0 538 L254 538 L254 410 Q150 440 60 450Z" fill="var(--green)"/>
      <circle cx="130" cy="145" r="115" fill="var(--cyan)"/>
      <circle cx="128" cy="152" r="116" fill="#222"/>
    </svg>
    <div class="photo" role="img" aria-label="Photo of a staff member helping two children at computers" style="left:14px;top:38px;width:230px;height:230px;border-radius:50%;background:linear-gradient(135deg,#6b6f73,#b8a288 45%,#3a8a5a)"></div>
    <div class="brand" style="left:70px;top:322px;color:var(--blue);font-size:12px"><span class="dot" style="background:var(--blue)"></span>BRIGHT PATH ACADEMY</div>
    <div class="title-box">
      <span class="line cyan">AFTER SCHOOL</span>
      <span class="line cyan">CURRICULUM</span>
      <span class="line big">GUIDE</span>
    </div>
    <p class="url" style="top:503px">www.brightpathacademy.org</p>
  </div>
</section>

<section class="spread inside">
  <div class="panel p1" style="background:var(--paper)">
    <svg class="deco" width="254" height="538" viewBox="0 0 254 538" aria-hidden="true">
      <path d="M160 0 Q200 40 254 30 L254 0Z" fill="var(--sky)"/>
    </svg>
    <h2 class="section" style="top:34px">PROGRAMS</h2>
    <p class="intro">The BRIGHT PATH ACADEMY is the after school program of the Youth Clubs of the Riverlands. We have a lineup of tested and nationally proven programs that address today’s most pressing youth issues, teaching young people the skills they need to succeed in life. We offer programs with a purpose in an affordable, safe, fun environment.</p>
    <p class="lead">Our programs revolve around five core areas of focus:</p>
    <ul class="core-list">
      <li><i></i>Character &amp; Leadership</li>
      <li><i></i>Health &amp; Life Skills</li>
      <li><i></i>Sports, Fitness, &amp; Recreation</li>
      <li><i></i>Education &amp; Career Development</li>
      <li><i></i>The Arts</li>
    </ul>
    <div style="position:absolute;left:26px;top:322px;width:194px;height:104px;background:var(--red);transform:rotate(-4deg)"></div>
    <div class="photo" role="img" aria-label="Photo of children dancing together in a school hallway" style="left:24px;top:318px;width:190px;height:100px;transform:rotate(-6deg);background:linear-gradient(135deg,#c9c4bc,#e8e2da 50%,#b03a44)"></div>
  </div>

  <div class="panel p2" style="background:var(--cyan)">
    <div class="card" style="left:24px;top:14px;width:206px;height:160px;padding:3px">
      <div class="photo" role="img" aria-label="Photo of three students working together at a computer" style="width:200px;height:102px;background:linear-gradient(135deg,#7e8fa3,#d0b8a4 50%,#2d4f9a)"></div>
      <div class="cap" style="background:var(--blue);height:52px"><b>98% of our participants plan to go beyond high school</b>I like the friendly staff and that they set aside time for homework. - BPA Parent</div>
    </div>
    <div class="card" style="left:24px;top:182px;width:206px;height:160px;padding:3px">
      <div class="photo" role="img" aria-label="Photo of a staff member talking with a student in a classroom" style="width:200px;height:130px;background:linear-gradient(135deg,#e8eaec,#c9cfd4 50%,#1f5f73)"></div>
      <div class="cap" style="background:var(--purple);height:24px">Our mission is to inspire and enable all young people to reach their full potential as caring citizens.</div>
    </div>
    <div class="card" style="left:24px;top:350px;width:206px;height:166px;padding:3px">
      <div class="photo" role="img" aria-label="Photo of a student and a mentor smiling together at a table" style="width:200px;height:136px;background:linear-gradient(135deg,#b9b2a8,#e0d6c8 50%,#4a6fa0)"></div>
      <div class="cap" style="background:var(--yellow);height:24px">Education &amp; Career Development programs help every member graduate ready for college or a career.</div>
    </div>
  </div>

  <div class="panel p3" style="background:var(--paper)">
    <svg class="deco" width="254" height="538" viewBox="0 0 254 538" aria-hidden="true">
      <path d="M0 0 H254 V40 Q200 20 150 30 Q90 40 40 10 Q20 0 0 20Z" fill="var(--sky)"/>
      <path d="M0 420 Q120 360 254 380 L254 538 L0 538Z" fill="var(--green)"/>
    </svg>
    <div class="card" style="left:22px;top:24px;width:200px;height:150px;transform:rotate(-3deg);padding:3px">
      <span class="tape"></span>
      <div class="photo" role="img" aria-label="Photo of a smiling boy holding a basketball" style="width:194px;height:102px;background:linear-gradient(135deg,#2a9b8f,#6bc3b8 50%,#e07a3a)"></div>
      <div class="cap" style="background:var(--green);height:40px"><b>Be Responsible Be Prepaid Be Educated</b>Programs in Health &amp; Life Skills build healthy habits, personal goals and a sense of well-being for life.</div>
    </div>
    <div class="card" style="left:22px;top:182px;width:196px;height:140px;transform:rotate(1deg);padding:3px">
      <span class="tape"></span>
      <div class="photo" role="img" aria-label="Photo of two boys posing in a gym" style="width:190px;height:100px;background:linear-gradient(135deg,#cfa977,#e8dcc6 50%,#2f6fc0)"></div>
      <div class="cap" style="background:var(--yellow);height:32px"><b>Be Fit Be Healthy Be Creative</b>Programs in Sports, Fitness &amp; Recreation build teamwork, healthy play and a lasting love of activity.</div>
    </div>
    <div class="card" style="left:20px;top:334px;width:204px;height:150px;transform:rotate(-4deg);padding:3px">
      <span class="tape"></span>
      <div class="photo" role="img" aria-label="Photo of children building a project together at a table" style="width:198px;height:100px;background:linear-gradient(135deg,#8a7a66,#d6c8b0 50%,#3a78c0)"></div>
      <div class="cap" style="background:var(--red);height:40px"><b>Be Positive Be Respectful Be Leader</b>Our Character &amp; Leadership programs help youth serve their community, lead with respect and make good choices.</div>
    </div>
  </div>
</section>

</body>
</html>
```